RJ Penhall & Associates

Create a website encompassing design work already carried out for business card.
Small accounting practice, business accounting and management, superannuation, audit, taxation.

```html
<!DOCTYPE html>
<html lang="en">
<head>
<meta charset="utf-8">
<title>RJ Penhall &amp; Associates</title>
<link rel="stylesheet" href="https://fonts.googleapis.com/css2?family=Open+Sans:wght@400;600&family=Arimo:wght@400&display=swap">
<style>
  :root {
    --page-bg: #f3f3f7;
    --outer-bg: #ffffff;
    --brand-blue: #3a9fd5;
    --heading-blue: #1b7ec2;
    --icon-navy: #1c557f;
    --text-dark: #2b2b2b;
    --text-body: #7a7a7a;
    --text-mid: #555555;
    --footer-bg: #3d3d3d;
    --footer-text: #a9a9a9;
    --frame: #ffffff;
    --frame-line: #dcdce2;
  }
  * { box-sizing: border-box; margin: 0; padding: 0; }
  html, body { width: 1200px; height: 1000px; overflow: hidden; background: var(--outer-bg); }
  body { position: relative; font-family: "Open Sans", Arial, sans-serif; color: var(--text-dark); }

  .page { position: absolute; left: 141px; top: 0; width: 912px; height: 1000px; background: var(--page-bg); border-top: 3px solid var(--brand-blue); }
  .abs { position: absolute; }

  /* header */
  .brand { left: 305px; top: 19px; display: flex; align-items: center; gap: 9px; }
  .brand-mark { width: 40px; height: 40px; background: var(--brand-blue); }
  .brand-name { font-family: "Open Sans", sans-serif; font-weight: 600; font-size: 15px; line-height: 17px; color: var(--text-dark); }
  .contact { left: 732px; top: 26px; font-size: 10.5px; line-height: 16px; color: var(--text-mid); }
  .contact-row { display: flex; align-items: center; gap: 6px; }
  .contact-row svg { width: 11px; height: 9px; fill: var(--brand-blue); }

  /* hero */
  .hero-shadow { left: 340px; top: 318px; width: 510px; height: 18px; background: radial-gradient(ellipse at center top, rgba(0,0,0,.28), rgba(0,0,0,0) 70%); }
  .hero-frame { left: 305px; top: 85px; width: 585px; height: 240px; background: var(--frame); border: 1px solid var(--frame-line); padding: 3px; }
  .hero-photo { width: 100%; height: 100%; background: linear-gradient(90deg, #8a8e99 0%, #c9ccd6 35%, #e6e7ec 55%, #b7a79a 75%, #d9d6d6 100%); }
  .hero-caption { left: 363px; top: 181px; }
  .hero-caption span { display: inline-block; background: rgba(240,236,232,.88); padding: 0 10px; font-size: 13px; line-height: 28px; text-transform: uppercase; }
  .cap-1 { color: #1a1a1a; }
  .cap-2 { color: var(--heading-blue); margin-top: 2px; }

  /* welcome */
  .welcome-title { left: 306px; top: 371px; font-family: "Arimo", Arial, sans-serif; font-size: 15px; color: var(--heading-blue); }
  .welcome-lead { left: 306px; top: 393px; font-family: "Arimo", Arial, sans-serif; font-size: 10px; color: var(--text-mid); }
  .welcome-frame { left: 305px; top: 427px; width: 179px; height: 97px; background: var(--frame); border: 1px solid var(--frame-line); padding: 4px; }
  .welcome-photo { width: 100%; height: 100%; background: linear-gradient(135deg, #27323f 0%, #6d7c8f 40%, #d9dde4 70%, #4a8ec8 100%); }
  .welcome-text { left: 502px; top: 424px; width: 388px; font-size: 8px; line-height: 12.6px; color: var(--text-body); }
  .welcome-text p + p { margin-top: 12.6px; }

  /* services */
  .services { left: 141px; top: 570px; width: 912px; height: 178px; background: var(--brand-blue); }
  .service-divider { top: 570px; width: 14px; height: 225px; background: linear-gradient(90deg, rgba(0,0,0,.06), rgba(0,0,0,0)); }
  .service { top: 0; width: 116px; text-align: center; color: #fff; }
  .service-icon { position: absolute; left: 38px; top: 30px; width: 40px; height: 40px; }
  .service-name { position: absolute; left: 0; width: 116px; font-family: "Arimo", Arial, sans-serif; font-size: 12px; line-height: 12px; }
  .read-more { position: absolute; left: 29px; top: 125px; width: 58px; height: 21px; border: 1px solid #fff; border-radius: 2px; font-family: "Arimo", Arial, sans-serif; font-size: 7px; line-height: 19px; color: #fff; }

  /* testimonials */
  .clients-title { left: 306px; top: 787px; font-family: "Arimo", Arial, sans-serif; font-size: 15px; color: var(--text-dark); }
  .avatar { top: 836px; width: 42px; height: 42px; border-radius: 50%; border: 2px solid #fff; background: radial-gradient(circle at 50% 45%, #c99a7b 0%, #8a6a55 55%, #e9e3dc 100%); }
  .avatar.active { border-color: var(--brand-blue); }
  .quote { left: 330px; top: 903px; width: 535px; text-align: center; font-size: 8px; line-height: 12.6px; color: var(--text-body); }
  .client-name { left: 330px; top: 932px; width: 535px; text-align: center; font-size: 8px; color: var(--heading-blue); }

  /* footer */
  .footer { left: 141px; top: 969px; width: 912px; height: 31px; background: var(--footer-bg); }
  .copyright { left: 306px; top: 983px; font-size: 8px; color: var(--footer-text); }
  .social { left: 803px; top: 981px; display: flex; gap: 4px; }
  .social span { width: 14px; height: 14px; background: #6a6a6a; }
</style>
</head>
<body>
  <div class="page"></div>

  <header>
    <div class="abs brand">
      <div class="brand-mark"></div>
      <div class="brand-name">RJ Penhall<br>&amp; Associates</div>
    </div>
    <div class="abs contact">
      <div class="contact-row"><svg viewBox="0 0 11 9"><path d="M0 0h11v9H0z M1 1.2v.6l4.5 3 4.5-3v-.6z" fill-rule="evenodd"/></svg>info@rjpenhallassociates.com</div>
      <div class="contact-row"><svg viewBox="0 0 11 9"><path d="M0 2.5C2 .5 9 .5 11 2.5L10 4H8V3H3v1H1z M2 5h7l1 4H1z"/></svg>123-456-0142</div>
    </div>
  </header>

  <section>
    <div class="abs hero-shadow"></div>
    <div class="abs hero-frame"><div class="hero-photo" role="img" aria-label="Office photo: smiling businessman in front, colleagues working at a laptop behind"></div></div>
    <div class="abs hero-caption">
      <span class="cap-1">Lorem Ipsum is simply dummy text of the</span><br>
      <span class="cap-2">Printing and typesetting</span>
    </div>
  </section>

  <section>
    <h1 class="abs welcome-title" style="font-weight:400">Welcome To RJ Penhall &amp; Associates</h1>
    <p class="abs welcome-lead">Lorem Ipsum is simply dummy text of the printing and typesetting industry.</p>
    <div class="abs welcome-frame"><div class="welcome-photo" role="img" aria-label="Photo of hands reviewing financial charts with a tablet"></div></div>
    <div class="abs welcome-text">
      <p>Lorem Ipsum is simply dummy text of the printing and typesetting industry. Lorem Ipsum has been the industry's standard dummy text ever since the 1500s, when an unknown printer took a galley of type and scrambled it to make a type specimen book. It has survived not only five centuries, but also the leap into electronic typesetting, remaining essentially unchanged.</p>
      <p>It was popularised in the 1960s with the release of Lettrafix sheets containing Lorem Ipsum passages, and more recently with desktop publishing software like Pressline Layout including versions of Lorem Ipsum.</p>
    </div>
  </section>

  <section class="abs services">
    <div class="abs service" style="left:165px">
      <svg class="service-icon" viewBox="0 0 40 40" fill="none" stroke="var(--icon-navy)" stroke-width="2.2"><rect x="7" y="3" width="22" height="32"/><path d="M12 10h12M12 15h12M12 20h9M12 28h6"/><path d="M22 31l9-9 3 3-9 9h-3z" fill="var(--icon-navy)"/></svg>
      <div class="service-name" style="top:86px">Accounting</div>
      <div class="read-more">READ MORE</div>
    </div>
    <div class="abs service" style="left:281px">
      <svg class="service-icon" viewBox="0 0 40 40" fill="var(--icon-navy)"><path d="M6 8h14v3H6z"/><path d="M9 4h26v22H9z" opacity=".85"/><path d="M3 14h13l2 3h18l-4 20H3z"/></svg>
      <div class="service-name" style="top:88px">Business<br>Management</div>
      <div class="read-more">READ MORE</div>
    </div>
    <div class="abs service" style="left:398px">
      <svg class="service-icon" viewBox="0 0 40 40" fill="var(--icon-navy)"><rect x="22" y="1" width="16" height="8" transform="rotate(40 30 5)"/><rect x="1" y="18" width="16" height="8" transform="rotate(40 9 22)"/><path d="M10 17l10-8 12 12-12 12z" opacity=".9"/></svg>
      <div class="service-name" style="top:83px">Audit</div>
      <div class="read-more">READ MORE</div>
    </div>
    <div class="abs service" style="left:514px">
      <svg class="service-icon" viewBox="0 0 40 40" fill="var(--icon-navy)"><circle cx="12" cy="9" r="7"/><circle cx="28" cy="9" r="7"/><path d="M0 36c0-12 6-18 12-18s12 6 12 18z"/><path d="M16 36c0-12 6-18 12-18s12 6 12 18z" opacity=".85"/></svg>
      <div class="service-name" style="top:83px">Superannuation</div>
      <div class="read-more">READ MORE</div>
    </div>
    <div class="abs service" style="left:631px">
      <svg class="service-icon" viewBox="0 0 40 40" fill="var(--icon-navy)"><text x="20" y="9" text-anchor="middle" font-family="Arimo, Arial, sans-serif" font-size="9" font-weight="700">TAX%</text><circle cx="20" cy="15" r="4"/><path d="M15 20h10v9h-3v9h-4v-9h-3z"/></svg>
      <div class="service-name" style="top:83px">Tax</div>
      <div class="read-more">READ MORE</div>
    </div>
  </section>
  <div class="abs service-divider" style="left:424px"></div>
  <div class="abs service-divider" style="left:540px"></div>
  <div class="abs service-divider" style="left:656px"></div>
  <div class="abs service-divider" style="left:772px"></div>

  <section>
    <h2 class="abs clients-title" style="font-weight:400">What Our Client Say About Us</h2>
    <div class="abs avatar" style="left:473px" role="img" aria-label="Client portrait"></div>
    <div class="abs avatar" style="left:525px" role="img" aria-label="Client portrait"></div>
    <div class="abs avatar active" style="left:576px" role="img" aria-label="Client portrait"></div>
    <div class="abs avatar" style="left:628px" role="img" aria-label="Client portrait"></div>
    <div class="abs avatar" style="left:679px" role="img" aria-label="Client portrait"></div>
    <p class="abs quote">Lorem Ipsum is simply dummy text of the printing and typesetting industry. Lorem Ipsum has been the industry's standard dummy text ever since the 1500s, when an unknown printer took a galley of type and scrambled it to make a type specimen book.</p>
    <p class="abs client-name">Client Name</p>
  </section>

  <footer>
    <div class="abs footer"></div>
    <p class="abs copyright">Copyright © 2014 RJ Penhall &amp; Associates .All Rights Reserved</p>
    <div class="abs social" aria-label="Social links"><span></span><span></span><span></span><span></span><span></span></div>
  </footer>
</body>
</html>
```